Buch-/E-Book-Cover für Sachbuch über Hunderasse
Zielgruppe
Ich benötige ein Buch-Cover im DIN A5 Format für ein anspruchsvolles Sachbuch, das die rassetypischen Krankheiten der Hunderasse Rhodesian Ridgeback thematisiert. Die Zielgruppe sind Züchter, Tierärzte und Liebhaber der Rasse.
Aufgabenstellung
Den größten Raum sollte ein Foto der Rasse einnehmen. Das Foto würde ich stellen, im Entwurf kann also ein Beispielfoto verwendet werden. Da das Buch der Auftakt zu einer Reihe ist, sollte das Design einen hohen Wiedererkennungswert haben und in erster Linie seriös wirken. Das Foto, der Rassename und die verwendeten Farben sollten leicht austauschbar sein. Sowohl der Titel als auch der Untertitel sind recht lang. Der Arbeitstitel lautet: Der Rhodesian Ridgeback zwischen Sprechstunde und Alltag, Untertitel: Ein Begleiter für Halter und Praxisteams.

```html
<!DOCTYPE html>
<html lang="de">
<head>
<meta charset="utf-8">
<title>Der Rhodesian Ridgeback zwischen Sprechstunde und Alltag – Cover</title>
<link rel="stylesheet" href="https://fonts.googleapis.com/css2?family=Catamaran:wght@300;400&display=swap">
<style>
  :root {
    --brown: #74401f;
    --brown-line: #8a5a3c;
    --accent: #e5501b;
    --paper: #ffffff;
    --coat-pale: #f1dcc4;
    --coat-light: #d9934e;
    --coat-mid: #b8702f;
    --coat-dark: #8e4c22;
    --text: #ffffff;
  }
  * { margin: 0; padding: 0; box-sizing: border-box; }
  html, body { width: 1200px; height: 750px; overflow: hidden; background: var(--paper); }
  body { font-family: "Catamaran", sans-serif; font-weight: 300; color: var(--text); }

  .cover { position: relative; width: 1200px; height: 750px; }

  .back-cover {
    position: absolute; left: 0; top: 0; width: 580px; height: 750px;
    background: var(--brown);
  }
  .back-title {
    position: absolute; left: 111px; top: 107px; width: 465px;
    font-size: 33px; line-height: 42px; font-weight: 300; white-space: nowrap;
  }
  .back-subtitle {
    position: absolute; left: 112px; top: 199px;
    font-size: 20px; line-height: 24px; font-weight: 300;
  }
  .back-blurb {
    position: absolute; left: 111px; top: 258px; width: 325px;
    font-size: 16px; line-height: 20px; font-weight: 300;
  }
  .isbn {
    position: absolute; left: 122px; top: 668px;
    font-size: 12.5px; line-height: 16px; font-weight: 300;
  }

  .spine {
    position: absolute; left: 580px; top: 0; width: 26px; height: 750px;
    background: var(--brown);
    border-left: 1px solid var(--brown-line);
    border-right: 1px solid var(--brown-line);
  }
  .spine-text {
    position: absolute; left: 50%; top: 714px;
    transform-origin: 0 0;
    transform: rotate(-90deg) translateY(-50%);
    white-space: nowrap;
    font-size: 11.5px; line-height: 1;
    display: flex; gap: 20px;
  }
  .spine-title { font-weight: 400; }
  .spine-subtitle { font-weight: 300; }

  .front-cover {
    position: absolute; left: 606px; top: 0; width: 594px; height: 750px;
    background: var(--paper); overflow: hidden;
  }
  .breed-photo {
    position: absolute; inset: 0;
    background:
      radial-gradient(ellipse 70% 85% at 52% 52%,
        var(--coat-light) 0%, var(--coat-mid) 40%, var(--coat-dark) 68%, var(--coat-pale) 100%);
  }
  .title-band {
    position: absolute; left: 0; top: 530px; width: 594px; height: 173px;
    background: var(--brown);
  }
  .title-band-accent {
    position: absolute; left: 44px; top: 1px; width: 10px; height: 171px;
    background: var(--accent);
  }
  .front-title {
    position: absolute; left: 93px; top: 22px; width: 495px;
    font-size: 35px; line-height: 48px; font-weight: 300; white-space: nowrap;
  }
  .front-subtitle {
    position: absolute; left: 95px; top: 124px;
    font-size: 22px; line-height: 26px; font-weight: 300; white-space: nowrap;
  }
</style>
</head>
<body>
<main class="cover">
  <section class="back-cover">
    <h2 class="back-title">Der Rhodesian Ridgeback<br>zwischen Sprechstunde und Alltag</h2>
    <p class="back-subtitle">Ein Begleiter für Halter und Praxisteams</p>
    <p class="back-blurb">Den größten Raum sollte ein Foto der Rasse einnehmen. Das Foto würde ich stellen, im Entwurf kann also ein Beispielfoto verwendet werden. Da das Buch der Auftakt zu einer Reihe ist, sollte das Design einen hohen Wiedererkennungswert haben und in erster Linie seriös wirken. Das Foto, der Rassename und die verwendeten Farben sollten leicht austauschbar sein. Sowohl der Titel als auch der Untertitel sind recht lang. Der Arbeitstitel lautet: Der Rhodesian Ridgeback zwischen Sprechstunde und Alltag, Untertitel: Ein Begleiter für Halter und Praxisteams.</p>
    <p class="isbn">ISBN 1234567889</p>
  </section>

  <section class="spine">
    <div class="spine-text">
      <span class="spine-title">Der Rhodesian Ridgeback zwischen Sprechstunde und Alltag</span>
      <span class="spine-subtitle">Ein Begleiter für Halter und Praxisteams</span>
    </div>
  </section>

  <section class="front-cover">
    <div class="breed-photo" role="img" aria-label="Großes Porträtfoto eines rotbraunen Rhodesian Ridgeback vor weißem Hintergrund, füllt die gesamte Vorderseite"></div>
    <div class="title-band">
      <div class="title-band-accent"></div>
      <h1 class="front-title">Der Rhodesian Ridgeback<br>zwischen Sprechstunde und Alltag</h1>
      <p class="front-subtitle">Ein Begleiter für Halter und Praxisteams</p>
    </div>
  </section>
</main>
</body>
</html>
```